App Design for FlavorTrek

We need an app design for a new app called FlavorTrek, which is an app designed to inspire exploration through personalized recipe generation, local restaurant discoveries, and a vibrant community platform. It caters to food enthusiasts looking to explore global cuisines or find the best local dining spots, offering a premium experience with selected features available for free.

-------UPDATED-----
This app will be AI Driven and may not be heavily dependent on media (images,videos) at first, especially for the Recipe generator feature. Our goal is to still have attractive UI. The core functionalities we are looking are the following
1. Recipe Generator: Either user choose a specific cuisine(italian,spanish), or user inputs ingredients and get recipe, or get recipe for different occasions (xmas, thanksgiving ) and get a randomly get recipe to cook, plain simple. We expect the recipes to be displayed in clear and not too generic manner starting with ingredients and expected duration at top and then step by step guide. We also intend to enable premium users to have playful action button or icon to get unlimited recipes generated until they find what they like and also have save for later feature. These premium features should be disabled for free users and prompted to subscribe if they click them with nice popup
2. Restaurant Recommendation - will have selected pictures and will be based on inputs such as zip code and other filters such as cousine types. Premium users can filter by price range, get unlimited recommendation, see actual price range in the recommendation and can save for later where they can find it later. Free users cannot filter by price (disabled) and should see it hidden in the recommendation
3. Meal Planning - will include just simple and random meal plan with just one button or limited interaction for free, users need to subscribe to get features such as customized plan such as considering allergies or diet preferences. Premium users can also get a shopping checklist of ingredients for weekly meal preps and their step by step guide for each meal recipe.
2. Community Sharing: users can view posts and engage with community content
Updates

Hello Designers,

The initial price was not fair for the work. So I have increased it. There will also be $50-100 bonus for those who come up with great designs or for those who incorporate interesting stuff. Thank you! Much appreciated 🙏

Colors
0054AA
0677BA
7BADD7
CADEEF
E8F1F8
0094D4
00A9DD
6FCCEA
C7EBF8
E9F6FB
00AB8E
00BBA5
67D7C9
C6EFE9
E9F9F6
FFC000
F8CF3A
FAE287
FDF2CF
FEFAEE
F0912C
F2A743
F7CA91
FBE8D2
FDF5EE
EE7325
F08F49
F5BC92
FAE3D3
FDF4ED
A7469A
B969AE
D3A5CF
EDDBEB
F8F0F9
6B429C
8869AF
B7A5CE
E3DAEB
F3F0F8

```html
<!DOCTYPE html>
<html lang="en">
<head>
<meta charset="utf-8">
<title>FlavorTrek – App Flow</title>
<link rel="stylesheet" href="https://fonts.googleapis.com/css2?family=Gilda+Display&family=Manrope:wght@400;500;600;700&display=swap">
<style>
:root{
  --bg:#c4c4c4;
  --ink:#141414;
  --muted:#8a8a8f;
  --frame:#ececf0;
  --screen:#f2f3f7;
  --white:#ffffff;
  --orange:#f7a400;
  --orange-soft:#fdf2cf;
  --line:#7f7f7f;
}
*{box-sizing:border-box;margin:0;padding:0}
html,body{width:1178px;height:1200px;overflow:hidden;background:var(--bg)}
.stage{position:absolute;left:0;top:0;width:1904px;height:1940px;transform:scale(.6187);transform-origin:0 0;font-family:'Manrope',sans-serif;color:var(--ink)}
.serif{font-family:'Gilda Display',serif;font-weight:400}
.abs{position:absolute}
.title{position:absolute;left:0;width:1904px;top:84px;text-align:center;font-size:84px;letter-spacing:-1px}
.step-label{position:absolute;top:277px;font-size:14px}
.phone{position:absolute;background:var(--frame);border-radius:20px;box-shadow:0 0 0 1px #dcdce2}
.screen{position:absolute;left:8px;top:10px;width:236px;background:var(--screen);border-radius:12px;overflow:hidden}
.status{position:absolute;left:10px;top:8px;width:216px;font-size:8px;font-weight:600;display:flex;justify-content:space-between}
.status svg{height:7px}
.avatar{position:absolute;left:10px;top:33px;width:28px;height:28px;border-radius:50%;background:radial-gradient(circle at 50% 40%,#d9b39c,#6b4a3a)}
.hello{position:absolute;left:48px;top:36px;font-size:8.5px;font-weight:700}
.loc{position:absolute;left:48px;top:49px;font-size:6px;color:#555;display:flex;align-items:center;gap:3px}
.loc i{width:5px;height:6px;background:var(--orange);border-radius:50% 50% 50% 0;transform:rotate(-45deg);display:inline-block}
.bell{position:absolute;left:200px;top:37px;width:18px;height:18px;border-radius:50%;background:var(--white);display:flex;align-items:center;justify-content:center}
.h-ai{position:absolute;left:0;width:236px;text-align:center;font-size:18px}
.sub{position:absolute;left:20px;width:196px;text-align:center;font-size:7.5px;line-height:1.7;color:var(--muted)}
.search{position:absolute;left:10px;width:216px;height:27px;background:var(--white);border-radius:3px;display:flex;align-items:center;font-size:7.5px}
.search .cuisine{width:62px;padding-left:10px;font-weight:600;border-right:1px solid #e6e6ea;height:15px;display:flex;align-items:center;gap:5px}
.search .cuisine::after{content:"";width:3px;height:3px;border-right:1px solid #aaa;border-bottom:1px solid #aaa;transform:rotate(45deg)}
.search .field{flex:1;padding-left:10px;color:#888}
.search .go{width:21px;height:21px;margin-right:3px;background:var(--orange);border-radius:2px;display:flex;align-items:center;justify-content:center}
.lead{position:absolute;left:10px;font-size:8.5px;font-weight:500}
.tile{position:absolute;width:57px;height:57px;border-radius:3px;background:linear-gradient(150deg,#5a3b24,#2a1c14);overflow:hidden}
.tile span{position:absolute;left:0;right:0;bottom:9px;text-align:center;color:#fff;font-size:7px;font-weight:600}
.crown-badge{position:absolute;right:4px;top:2px;width:12px;height:12px;border-radius:2px;background:var(--orange);display:flex;align-items:center;justify-content:center}
.art{position:absolute;background:linear-gradient(135deg,#f3e3d8,#c9d8ea);border-radius:6px}
.tabbar{position:absolute;left:0;bottom:0;width:236px;height:62px}
.tab{position:absolute;bottom:6px;width:50px;margin-left:-25px;text-align:center;font-size:6.5px;color:#9a9a9f}
.tab svg{display:block;margin:0 auto 6px;width:16px;height:16px}
.tab.active .dot{width:36px;height:36px;border-radius:50%;background:var(--orange);margin:0 auto 10px;display:flex;align-items:center;justify-content:center;box-shadow:0 4px 8px rgba(247,164,0,.35)}
.tab.active{color:var(--orange)}
.photo{position:absolute;border-radius:3px}
.p-red{background:radial-gradient(circle at 50% 55%,#c9502a,#7a2d18 55%,#e8e3dc 80%)}
.p-green{background:radial-gradient(circle at 50% 50%,#e9d9a0,#8a9c52 55%,#3f4d2a)}
.p-fish{background:radial-gradient(circle at 50% 55%,#c78a5a,#7b5a3f 50%,#2a2320)}
.p-souffle{background:radial-gradient(circle at 45% 45%,#e9b35a,#9bc35c 55%,#eef2e6)}
.p-curry{background:radial-gradient(circle at 55% 45%,#d9731f,#6b2c14 55%,#2b211c)}
.p-dark{background:radial-gradient(circle at 50% 60%,#b4622e,#3b2317 60%,#17120f)}
.rcard{position:absolute;width:100px;height:127px;background:var(--white);border-radius:4px;overflow:hidden}
.rcard .photo{left:0;top:0;width:100px;height:77px;border-radius:0}
.rcard h4{position:absolute;left:8px;top:85px;font-size:8px;font-weight:600;line-height:1.6}
.meta{position:absolute;left:8px;right:6px;bottom:6px;display:flex;justify-content:space-between;font-size:6px;color:#777}
.meta b{font-weight:500}
.meta b::before{content:"★ ";color:var(--orange)}
.prem{position:absolute;left:0;top:0;padding:2px 5px;background:var(--orange);color:#fff;font-size:5.5px;border-radius:0 0 4px 0}
.save{position:absolute;width:11px;height:11px;border-radius:50%;background:#fff;border:1px solid var(--orange);display:flex;align-items:center;justify-content:center}
.save::before{content:"";width:4px;height:5px;background:var(--orange);clip-path:polygon(0 0,100% 0,100% 100%,50% 70%,0 100%)}
.btn{position:absolute;background:var(--orange);color:#fff;font-weight:600;border-radius:2px;display:flex;align-items:center;justify-content:center;gap:6px}
.note{position:absolute;font-size:20px;line-height:1.45}
.caption{position:absolute;left:0;width:1904px;text-align:center;top:1256px;font-size:29px}
.feat-ico{position:absolute;border-radius:50%;background:var(--white);display:flex;align-items:center;justify-content:center}
.feat{position:absolute;font-size:30px;white-space:nowrap}
.thanks{position:absolute;left:0;width:1904px;text-align:center;top:1686px;font-size:98px}
.ben{position:absolute;left:13px;width:162px;height:30px;display:flex;align-items:center;gap:10px;font-size:8px;font-weight:600;border-bottom:1px solid #e5e6ea}
.ben svg{width:13px;height:13px}
.litem{position:absolute;left:10px;width:216px;height:71px;background:var(--white);border-radius:4px}
.litem .photo{left:8px;top:6px;width:56px;height:60px}
.litem h5{position:absolute;left:72px;top:9px;font-size:8.5px;font-weight:500}
.litem p{position:absolute;left:72px;top:26px;width:122px;font-size:6px;line-height:1.6;color:#888}
.litem .rt{position:absolute;left:72px;top:54px;font-size:6px;color:#888}
.litem .rt b{color:var(--ink);font-weight:600}
.litem .rt b::before{content:"★ ";color:var(--orange)}
</style>
</head>
<body>
<div class="stage">

<svg width="0" height="0" style="position:absolute">
  <defs>
    <symbol id="i-bell" viewBox="0 0 20 20"><path d="M5 14V9a5 5 0 0 1 10 0v5l1.5 1.5h-13z" fill="#111"/><circle cx="14.5" cy="5.5" r="3.2" fill="#f7a400"/><rect x="8" y="16.5" width="4" height="1.6" rx=".8" fill="#111"/></symbol>
    <symbol id="i-crown" viewBox="0 0 20 20"><path d="M3 7l4 3 3-6 3 6 4-3-1.5 8h-11z" fill="currentColor"/></symbol>
    <symbol id="i-spark" viewBox="0 0 20 20"><path d="M5 5l10 10M15 5L5 15M10 3v3M10 14v3" stroke="#fff" stroke-width="1.6" fill="none"/></symbol>
    <symbol id="i-rest" viewBox="0 0 20 20"><path d="M3 8h14M4 8l2-4h8l2 4M5 8v9h10V8M9 17v-4h2v4" stroke="#9a9a9f" stroke-width="1.1" fill="none"/></symbol>
    <symbol id="i-recipe" viewBox="0 0 20 20"><rect x="4" y="3" width="12" height="14" rx="1.5" stroke="#fff" stroke-width="1.4" fill="none"/><path d="M7 7h6M7 10h6M7 13h4" stroke="#fff" stroke-width="1.4"/></symbol>
    <symbol id="i-home" viewBox="0 0 20 20"><path d="M3 9l7-6 7 6v8H3z M8 17v-5h4v5" stroke="#9a9a9f" stroke-width="1.1" fill="none"/></symbol>
    <symbol id="i-comm" viewBox="0 0 20 20"><circle cx="10" cy="10" r="7" stroke="#9a9a9f" stroke-width="1.1" fill="none"/><circle cx="10" cy="8" r="2" stroke="#9a9a9f" fill="none"/><circle cx="6" cy="11" r="1.5" stroke="#9a9a9f" fill="none"/><circle cx="14" cy="11" r="1.5" stroke="#9a9a9f" fill="none"/></symbol>
    <symbol id="i-prof" viewBox="0 0 20 20"><circle cx="10" cy="7" r="3.5" stroke="#9a9a9f" stroke-width="1.1" fill="none"/><path d="M4 17c0-4 3-6 6-6s6 2 6 6z" stroke="#9a9a9f" stroke-width="1.1" fill="none"/></symbol>
    <symbol id="i-status" viewBox="0 0 40 10"><path d="M2 5a6 6 0 0 1 8 0M4 7a3 3 0 0 1 4 0" stroke="#111" fill="none"/><rect x="15" y="6" width="1.5" height="3" fill="#111"/><rect x="18" y="3" width="1.5" height="6" fill="#111"/><rect x="21" y="1" width="1.5" height="8" fill="#111"/><rect x="27" y="2" width="10" height="6" rx="1" stroke="#111" fill="none"/><rect x="28.5" y="3.5" width="6" height="3" fill="#111"/></symbol>
  </defs>
</svg>

<h1 class="title serif">FlavorTrek</h1>

<div class="step-label serif" style="left:175px">01.Recipe Generator</div>
<div class="step-label serif" style="left:509px">02.Animation Loading</div>
<div class="step-label serif" style="left:825px">03.Search Results</div>
<div class="step-label serif" style="left:1144px">04.Premium Popup</div>
<div class="step-label serif" style="left:1476px">05.Italian Recipe</div>

<svg class="abs" style="left:0;top:0" width="1904" height="1940" fill="none" stroke="var(--line)" stroke-width="1">
  <path d="M196 538H153M157 534l-4 4 4 4"/>
  <path d="M194 640H117V1303H1532V1186M1528 1190l4-4 4 4"/>
  <path d="M194 732H117"/>
  <path d="M402 711H502M498 707l4 4-4 4"/>
  <path d="M742 551H820M816 547l4 4-4 4"/>
  <path d="M1043 976H1262V853M1258 857l4-4 4 4"/>
  <path d="M1030 995V1030H1130M1126 1026l4 4-4 4"/>
</svg>
<div class="note serif" style="left:60px;top:519px;font-size:11px;line-height:1.5">User can select<br>cuisine here</div>
<div class="note serif" style="left:1144px;top:1010px">search results restricted for<br>normal user</div>

<!-- 01 Recipe Generator -->
<div class="phone" style="left:175px;top:313px;width:253px;height:593px">
  <div class="screen" style="height:573px">
    <div class="status"><span>5:50 am</span><svg viewBox="0 0 40 10" width="30"><use href="#i-status"/></svg></div>
    <div class="avatar" role="img" aria-label="User profile photo"></div>
    <div class="hello">Hello Mira</div>
    <div class="loc"><i></i>Linden Row, Easton</div>
    <div class="bell"><svg width="12" height="12"><use href="#i-bell"/></svg></div>
    <div class="h-ai serif" style="top:124px">AI Recipe Generator</div>
    <div class="sub" style="top:156px">The best AI recipe generator. Enter ingredients and get recipes with our cooking AI.</div>
    <div class="search" style="top:202px"><div class="cuisine">Cuisine</div><div class="field">Please enter ingredients</div><div class="go"><svg width="10" height="10"><use href="#i-spark"/></svg></div></div>
    <div class="lead" style="top:253px">Choose a cuisine to get started.</div>
    <div class="tile" style="left:10px;top:279px" role="img" aria-label="Italian dishes with map outline"><div class="crown-badge"><svg width="8" height="8" style="color:#fff"><use href="#i-crown"/></svg></div><span>Italian</span></div>
    <div class="tile" style="left:72px;top:279px" role="img" aria-label="Spanish dishes with map outline"><span>Spanish</span></div>
    <div class="tile" style="left:134px;top:279px" role="img" aria-label="Indian dishes with map outline"><span>Indian</span></div>
    <div class="tile" style="left:196px;top:279px" role="img" aria-label="Australian dishes with map outline"><span>Australia</span></div>
    <div class="lead" style="top:349px">Choose a occasions to get started.</div>
    <div class="tile" style="left:10px;top:375px" role="img" aria-label="Christmas dishes with tree icon"><span>Xmas</span></div>
    <div class="tile" style="left:73px;top:375px" role="img" aria-label="Thanksgiving dishes with turkey icon"><span>Thanksgiving</span></div>
    <nav class="tabbar">
      <div class="tab" style="left:26px"><svg><use href="#i-rest"/></svg>Restaurant</div>
      <div class="tab active" style="left:71px"><div class="dot"><svg width="18" height="18" style="margin:0"><use href="#i-recipe"/></svg></div>Recipe</div>
      <div class="tab" style="left:119px"><svg><use href="#i-home"/></svg>Home</div>
      <div class="tab" style="left:171px"><svg><use href="#i-comm"/></svg>Community</div>
      <div class="tab" style="left:217px"><svg><use href="#i-prof"/></svg>Profile</div>
    </nav>
  </div>
</div>

<!-- 02 Animation Loading -->
<div class="phone" style="left:506px;top:313px;width:253px;height:593px">
  <div class="screen" style="height:573px">
    <div class="status"><span>5:50 am</span><svg viewBox="0 0 40 10" width="30"><use href="#i-status"/></svg></div>
    <div class="avatar" role="img" aria-label="User profile photo"></div>
    <div class="hello">Hello Mira</div>
    <div class="loc"><i></i>Linden Row, Easton</div>
    <div class="bell"><svg width="12" height="12"><use href="#i-bell"/></svg></div>
    <div class="art" style="left:82px;top:82px;width:76px;height:45px" role="img" aria-label="Cooking book and chef animation illustration"></div>
    <div class="h-ai serif" style="top:138px">AI Recipe Generator</div>
    <div class="sub" style="top:169px">The best AI recipe generator. Enter ingredients and get recipes with our cooking AI.</div>
    <div class="search" style="top:213px"><div class="cuisine">Cuisine</div><div class="field" style="color:#333">Chicken with rice</div><div class="go"><svg width="10" height="10"><use href="#i-spark"/></svg></div></div>
    <div class="lead" style="top:258px">Choose a cuisine to get started.</div>
    <div class="tile" style="left:10px;top:284px" role="img" aria-label="Italian dishes with map outline"><div class="crown-badge"><svg width="8" height="8" style="color:#fff"><use href="#i-crown"/></svg></div><span>Italian</span></div>
    <div class="tile" style="left:72px;top:284px" role="img" aria-label="Spanish dishes with map outline"><span>Spanish</span></div>
    <div class="tile" style="left:134px;top:284px" role="img" aria-label="Indian dishes with map outline"><span>Indian</span></div>
    <div class="tile" style="left:196px;top:284px" role="img" aria-label="Australian dishes with map outline"><span>Australia</span></div>
    <div class="lead" style="top:354px">Choose a occasions to get started.</div>
    <div class="tile" style="left:10px;top:380px" role="img" aria-label="Christmas dishes with tree icon"><span>Xmas</span></div>
    <div class="tile" style="left:73px;top:380px" role="img" aria-label="Thanksgiving dishes with turkey icon"><span>Thanksgiving</span></div>
    <nav class="tabbar">
      <div class="tab" style="left:26px"><svg><use href="#i-rest"/></svg>Restaurant</div>
      <div class="tab active" style="left:71px"><div class="dot"><svg width="18" height="18" style="margin:0"><use href="#i-recipe"/></svg></div>Recipe</div>
      <div class="tab" style="left:119px"><svg><use href="#i-home"/></svg>Home</div>
      <div class="tab" style="left:171px"><svg><use href="#i-comm"/></svg>Community</div>
      <div class="tab" style="left:217px"><svg><use href="#i-prof"/></svg>Profile</div>
    </nav>
  </div>
</div>

<!-- 03 Search Results -->
<div class="phone" style="left:825px;top:313px;width:253px;height:820px">
  <div class="screen" style="height:800px">
    <div class="status"><span>5:50 am</span><svg viewBox="0 0 40 10" width="30"><use href="#i-status"/></svg></div>
    <div class="avatar" role="img" aria-label="User profile photo"></div>
    <div class="hello">Hello Mira</div>
    <div class="loc"><i></i>Linden Row, Easton</div>
    <div class="bell"><svg width="12" height="12"><use href="#i-bell"/></svg></div>
    <div class="h-ai serif" style="top:87px">AI Recipe Generator</div>
    <div class="sub" style="top:118px">The best AI recipe generator. Enter ingredients and get recipes with our cooking AI.</div>
    <div class="search" style="top:165px"><div class="cuisine">Cuisine</div><div class="field" style="color:#333">Chicken with rice</div><div class="go"><svg width="10" height="10"><use href="#i-spark"/></svg></div></div>
    <div class="abs serif" style="left:10px;top:210px;font-size:11px">Search Results</div>

    <div class="rcard" style="left:10px;top:240px"><div class="photo p-red" role="img" aria-label="Honey chilli potatoes on a plate"></div><div class="prem">♛ Premium</div><div class="save" style="left:84px;top:71px"></div><h4>Honey Chilli<br>Potatoes</h4><div class="meta"><span>◷ 65 Mins</span><b>4.8</b></div></div>
    <div class="rcard" style="left:125px;top:240px"><div class="photo p-green" role="img" aria-label="East west spring rolls with greens"></div><h4>East West<br>Spring Rolls</h4><div class="meta"><span>◷ 20 Mins</span><b>4.8</b></div></div>
    <div class="rcard" style="left:10px;top:385px"><div class="photo p-fish" role="img" aria-label="Grilled citrus fish fillets"></div><h4>Grilled Citrus<br>Fish</h4><div class="meta"><span>◷ 40 Mins</span><b>4.8</b></div></div>
    <div class="rcard" style="left:125px;top:385px"><div class="photo p-souffle" role="img" aria-label="Cheese souffle in a green dish with apple"></div><div class="prem">♛ Premium</div><div class="save" style="left:84px;top:71px"></div><h4>Cheese Souffles<br>with Apple</h4><div class="meta"><span>◷ 35 Mins</span><b>4.5</b></div></div>

    <div class="rcard" style="left:10px;top:530px;opacity:.25"><div class="photo p-red" role="img" aria-label="Blurred recipe photo"></div></div>
    <div class="rcard" style="left:125px;top:530px;opacity:.25"><div class="photo p-green" role="img" aria-label="Blurred recipe photo"></div></div>
    <div class="rcard" style="left:10px;top:675px;opacity:.25"><div class="photo p-fish" role="img" aria-label="Blurred recipe photo"></div></div>
    <div class="rcard" style="left:125px;top:675px;opacity:.25"><div class="photo p-souffle" role="img" aria-label="Blurred recipe photo"></div></div>
    <div class="abs" style="left:0;top:525px;width:236px;height:275px;background:linear-gradient(rgba(242,243,247,.75),rgba(242,243,247,.85))"></div>
    <div class="abs serif" style="left:0;top:559px;width:236px;text-align:center;font-size:19px">Hello Mira</div>
    <div class="abs" style="left:0;top:594px;width:236px;text-align:center;font-size:9px;line-height:2.1">You have free membership plan.<br>Buy Premium plan to access the all recipe</div>
    <div class="btn" style="left:27px;top:640px;width:182px;height:30px;font-size:9.5px"><svg width="12" height="12" style="color:#fff"><use href="#i-crown"/></svg>Upgrade to Premium</div>

    <nav class="tabbar">
      <div class="tab" style="left:26px"><svg><use href="#i-rest"/></svg>Restaurant</div>
      <div class="tab active" style="left:71px"><div class="dot"><svg width="18" height="18" style="margin:0"><use href="#i-recipe"/></svg></div>Recipe</div>
      <div class="tab" style="left:119px"><svg><use href="#i-home"/></svg>Home</div>
      <div class="tab" style="left:171px"><svg><use href="#i-comm"/></svg>Community</div>
      <div class="tab" style="left:217px"><svg><use href="#i-prof"/></svg>Profile</div>
    </nav>
  </div>
</div>

<!-- 04 Premium Popup -->
<div class="phone" style="left:1144px;top:313px;width:253px;height:532px">
  <div class="screen" style="height:512px">
    <div class="status"><span>5:50 am</span><svg viewBox="0 0 40 10" width="30"><use href="#i-status"/></svg></div>
    <div class="avatar" role="img" aria-label="User profile photo"></div>
    <div class="hello">Hello Mira</div>
    <div class="loc"><i></i>Linden Row, Easton</div>
    <div class="bell"><svg width="12" height="12"><use href="#i-bell"/></svg></div>
    <div class="rcard" style="left:10px;top:385px"><div class="photo p-fish" role="img" aria-label="Grilled citrus fish fillets"></div><h4>Grilled Citrus<br>Fish</h4><div class="meta"><span>◷ 40 Mins</span><b>4.8</b></div></div>
    <div class="rcard" style="left:125px;top:385px"><div class="photo p-souffle" role="img" aria-label="Cheese souffle in a green dish"></div><h4>Cheese Souffles<br>with Apple</h4><div class="meta"><span>◷ 35 Mins</span><b>4.5</b></div></div>
    <div class="abs" style="left:0;top:0;width:236px;height:512px;background:rgba(70,70,70,.55)"></div>

    <div class="abs" style="left:9px;top:95px;width:216px;height:330px;background:var(--white);border-radius:12px">
      <div class="photo p-curry" style="left:6px;top:7px;width:44px;height:28px" role="img" aria-label="Soup bowl"></div>
      <div class="photo p-red" style="left:55px;top:7px;width:46px;height:28px" role="img" aria-label="Pasta dish"></div>
      <div class="photo p-souffle" style="left:106px;top:7px;width:56px;height:28px" role="img" aria-label="Baked gratin"></div>
      <div class="photo p-fish" style="left:167px;top:7px;width:44px;height:28px" role="img" aria-label="Grilled salmon"></div>
      <div class="abs" style="left:6px;top:40px;width:91px;height:27px;background:var(--orange);border-radius:3px;color:#fff;display:flex;align-items:center;gap:6px;padding-left:12px;font-family:'Gilda Display',serif;font-size:11px"><svg width="14" height="14" style="color:#fff"><use href="#i-crown"/></svg>Premium</div>
      <div class="photo p-red" style="left:102px;top:40px;width:48px;height:27px" role="img" aria-label="Tomato dish"></div>
      <div class="photo p-curry" style="left:155px;top:40px;width:56px;height:27px" role="img" aria-label="Curry dish"></div>
      <div class="abs" style="left:11px;top:77px;width:194px;height:240px;background:#f4f5f8;border-radius:10px">
        <div class="abs" style="right:8px;top:8px;width:9px;height:9px;border-radius:50%;background:#ddd"></div>
        <div class="abs serif" style="left:13px;top:16px;font-size:13px">Premium Benefits</div>
        <div class="abs" style="left:13px;top:40px;font-size:8px;color:var(--muted)">Try 2 months of Premium for $75</div>
        <div class="ben" style="top:62px"><svg viewBox="0 0 20 20"><path d="M3 9h14l-2 7H5zM7 9V5M10 9V3M13 9V5" stroke="#111" fill="none" stroke-width="1.3"/></svg>More Recipe, No more Limits</div>
        <div class="ben" style="top:92px"><svg viewBox="0 0 20 20"><path d="M5 3h10v14l-5-4-5 4z" stroke="#111" fill="none" stroke-width="1.3"/></svg>Save later option</div>
        <div class="ben" style="top:120px"><svg viewBox="0 0 20 20"><rect x="3" y="4" width="14" height="11" rx="1" stroke="#111" fill="none" stroke-width="1.3"/><path d="M9 7l4 2.5-4 2.5z" fill="#111"/></svg>Recipe making video</div>
        <div class="ben" style="top:151px;border-bottom:none"><svg viewBox="0 0 20 20"><path d="M5 3v14M10 3v14M15 3v14" stroke="#111" stroke-width="1.3"/><circle cx="5" cy="7" r="1.8" fill="#fff" stroke="#111"/><circle cx="10" cy="12" r="1.8" fill="#fff" stroke="#111"/><circle cx="15" cy="8" r="1.8" fill="#fff" stroke="#111"/></svg>Filter Option</div>
        <div class="btn" style="left:13px;top:194px;width:162px;height:27px;font-size:8.5px"><svg width="11" height="11" style="color:#fff"><use href="#i-crown"/></svg>Upgrade to Premium</div>
      </div>
    </div>
  </div>
</div>

<!-- 05 Italian Recipe -->
<div class="phone" style="left:1476px;top:313px;width:253px;height:865px">
  <div class="screen" style="height:845px">
    <div class="status"><span>5:50 am</span><svg viewBox="0 0 40 10" width="30"><use href="#i-status"/></svg></div>
    <div class="avatar" role="img" aria-label="User profile photo"></div>
    <div class="hello">Hello Mira</div>
    <div class="loc"><i></i>Linden Row, Easton</div>
    <div class="abs" style="left:10px;top:75px;width:184px;height:27px;background:var(--white);border-radius:3px;font-size:6.5px;color:#888;display:flex;align-items:center;justify-content:space-between;padding:0 8px 0 11px">Please enter ingredients<svg width="9" height="9" viewBox="0 0 10 10"><circle cx="4" cy="4" r="3" stroke="#333" fill="none"/><path d="M6.5 6.5L9 9" stroke="#333"/></svg></div>
    <div class="btn" style="left:201px;top:75px;width:27px;height:27px"><svg width="13" height="13" viewBox="0 0 20 20"><path d="M3 5h14M3 10h14M3 15h14" stroke="#111" stroke-width="1.4"/><rect x="11" y="3" width="3" height="4" fill="#fff" stroke="#111"/><rect x="5" y="8" width="3" height="4" fill="#fff" stroke="#111"/><rect x="12" y="13" width="3" height="4" fill="#fff" stroke="#111"/></svg></div>
    <div class="abs serif" style="left:10px;top:117px;font-size:14px">Italian Recipes</div>
    <div class="abs" style="left:8px;top:147px;width:220px;height:102px;border-radius:4px;background:linear-gradient(90deg,#232323 40%,#3b3a38)">
      <div class="photo" style="left:102px;top:4px;width:96px;height:96px;border-radius:50%;background:radial-gradient(circle,#e27b2e,#e6c06a 55%,#d9cfb5 70%,#2a2a2a 72%)" role="img" aria-label="Meatballs in tomato sauce over mashed potatoes"></div>
      <div class="abs serif" style="left:9px;top:28px;font-size:10.5px;color:#fff;line-height:1.35">Meatballs<br>in tomato sauce</div>
      <div class="btn" style="left:9px;top:64px;width:34px;height:12px;font-size:5.5px;border-radius:6px;color:#111">Details</div>
    </div>
    <div class="abs serif" style="left:10px;top:268px;font-size:10.5px">Popular  Recipes</div>
    <div class="abs" style="left:192px;top:271px;font-size:5.5px;color:#999">View All ›</div>
    <div class="abs" style="left:10px;top:294px;width:133px;height:118px;background:var(--white);border-radius:4px;overflow:hidden">
      <div class="photo p-curry" style="left:0;top:0;width:133px;height:69px;border-radius:0" role="img" aria-label="Dhal spicy curry in a pan"></div>
      <div class="prem">♛ Premium</div><div class="save" style="left:113px;top:63px"></div>
      <div class="abs" style="left:8px;top:77px;font-size:8px;font-weight:600">Dhal spicy curry</div>
      <div class="abs" style="left:8px;top:91px;width:120px;font-size:5.8px;color:#888;line-height:1.6">Lorem ipsum dolor sit amet, coect etuer adipiscing elit</div>
    </div>
    <div class="abs" style="left:156px;top:294px;width:133px;height:118px;background:var(--white);border-radius:4px;overflow:hidden">
      <div class="photo p-dark" style="left:0;top:0;width:133px;height:69px;border-radius:0" role="img" aria-label="Rustic meal cooked in a pan by candlelight"></div>
      <div class="abs" style="left:8px;top:77px;font-size:8px;font-weight:600">Rustic meal cooked</div>
      <div class="abs" style="left:8px;top:91px;width:120px;font-size:5.8px;color:#888;line-height:1.6">Lorem ipsum dolor sit etuer adipiscing elit</div>
    </div>
    <div class="abs serif" style="left:10px;top:431px;font-size:10.5px">Recommend for you</div>

    <div class="litem" style="top:454px"><div class="photo p-red" role="img" aria-label="Bowl of Sunday chili"></div><div class="crown-badge" style="left:12px;top:9px;right:auto;width:10px;height:10px"><svg width="7" height="7" style="color:#fff"><use href="#i-crown"/></svg></div><h5>The Best Sunday Chili</h5><div class="save" style="left:196px;top:8px"></div><p>This is the BEST Sunday Chili! Beef, bacon, tomatoes, chopped veggies...</p><div class="rt"><b>4.8</b>  (233 Ratings)</div></div>
    <div class="litem" style="top:533px"><div class="photo p-curry" role="img" aria-label="Hummus soup in a bowl"></div><h5>Hummus Soup</h5><p>This is the BEST Sunday Chili! Beef, bacon, tomatoes, chopped veggies...</p><div class="rt"><b>4.8</b>  (233 Ratings)</div></div>
    <div class="litem" style="top:612px"><div class="photo p-souffle" role="img" aria-label="Baked pasta casserole"></div><h5>Harvest Baked Casserole</h5><p>This is the BEST Sunday Chili! Beef, bacon, tomatoes, chopped veggies...</p><div class="rt"><b>4.8</b>  (233 Ratings)</div></div>
    <div class="litem" style="top:691px"><div class="photo p-red" role="img" aria-label="Barbecue chicken sandwich"></div><div class="crown-badge" style="left:12px;top:9px;right:auto;width:10px;height:10px"><svg width="7" height="7" style="color:#fff"><use href="#i-crown"/></svg></div><h5>Stovetop Barbecue Chken</h5><div class="save" style="left:196px;top:8px"></div><p>This is the BEST Sunday Chili! Beef, bacon, tomatoes, chopped veggies...</p><div class="rt"><b>4.8</b>  (233 Ratings)</div></div>

    <nav class="tabbar">
      <div class="tab" style="left:26px"><svg><use href="#i-rest"/></svg>Restaurant</div>
      <div class="tab active" style="left:71px"><div class="dot"><svg width="18" height="18" style="margin:0"><use href="#i-recipe"/></svg></div>Recipe</div>
      <div class="tab" style="left:119px"><svg><use href="#i-home"/></svg>Home</div>
      <div class="tab" style="left:171px"><svg><use href="#i-comm"/></svg>Community</div>
      <div class="tab" style="left:217px"><svg><use href="#i-prof"/></svg>Profile</div>
    </nav>
  </div>
</div>

<p class="caption serif">When user click Italian cuisine, this screen show all Italian receipe</p>

<div class="feat-ico" style="left:220px;top:1432px;width:82px;height:82px"><svg width="42" height="42"><use href="#i-bell"/></svg></div>
<div class="feat serif" style="left:339px;top:1454px">Notification : Will get new recipe alert</div>
<div class="feat-ico" style="left:950px;top:1437px;width:74px;height:74px"><svg width="36" height="36" viewBox="0 0 20 20"><rect x="2" y="2" width="16" height="16" rx="4" fill="#f7a400"/><path d="M7 6h6v8l-3-2.4L7 14z" fill="none" stroke="#fff" stroke-width="1.6" stroke-linejoin="round"/></svg></div>
<div class="feat serif" style="left:1065px;top:1456px">Save later Option</div>
<div class="feat-ico" style="left:1446px;top:1436px;width:74px;height:74px"><svg width="40" height="40" style="color:var(--orange)"><use href="#i-crown"/></svg></div>
<div class="feat serif" style="left:1562px;top:1454px">Premium</div>

<p class="abs serif" style="left:247px;top:1577px;font-size:29px">** Animation loading sample linked in comments</p>

<p class="thanks serif">Thanks for watching</p>
</div>
</body>
</html>
```